Consulting Company Business Card

I am looking for a minimalist, classy, professional design on my business card. I would like it to be double-sided. I want to use the font and color scheme of my logo which are attached. Please be creative in the designs that you send me. I want to play off the design of my logo with the inner C that is Green and Blue broken up with the white.
Target Market(s)
Small Businesses
Industry/Entity Type
Consulting
Contact Information for Business Card
Derek L. Whitmore, CPA CGMA, 555-014-2283, dwhitmore@brovantadvisory.example, www.brovantadvisory.example

```html
<!DOCTYPE html>
<html lang="en">
<head>
<meta charset="utf-8">
<title>Brovant Advisory – Business Card</title>
<link href="https://fonts.googleapis.com/css2?family=Montserrat:wght@400;500;700;800&display=swap" rel="stylesheet">
<style>
  :root {
    --navy: #232c4f;
    --teal: #2a8c86;
    --grey-text: #4a4f5c;
    --paper: #ffffff;
    --backdrop: #bfbfbf;
  }
  * { box-sizing: border-box; margin: 0; padding: 0; }
  html, body {
    width: 1200px; height: 788px; overflow: hidden;
    background: var(--backdrop);
    font-family: "Montserrat", sans-serif;
  }
  .sheet {
    width: 1200px; height: 788px;
    display: flex; align-items: center; justify-content: center; gap: 44px;
  }
  .card {
    position: relative;
    width: 530px; height: 303px;
    border-radius: 26px;
    overflow: hidden;
    box-shadow: 0 10px 24px rgba(0,0,0,0.22);
  }
  .card--front { background: var(--paper); }
  .card--back { background: var(--navy); }

  .corner-tab {
    position: absolute; top: 0; right: 58px;
    width: 22px; height: 30px; background: var(--navy);
  }
  .holder {
    position: absolute; top: 46px; right: 44px; text-align: right;
  }
  .holder__name {
    font-weight: 800; font-size: 25px; letter-spacing: 1.5px;
    color: var(--navy); text-transform: uppercase;
  }
  .holder__name .surname { color: var(--teal); }
  .holder__title {
    margin-top: 4px; font-weight: 400; font-size: 14px;
    letter-spacing: 1px; color: var(--grey-text);
  }

  .brand {
    display: flex; align-items: center; gap: 10px;
    font-weight: 800; text-transform: uppercase; letter-spacing: 2px;
  }
  .brand__dot { border-radius: 50%; flex: none; }
  .card--front .brand {
    position: absolute; left: 38px; top: 132px;
    font-size: 22px; color: var(--navy);
  }
  .card--front .brand__dot { width: 18px; height: 18px; background: var(--navy); }

  .contacts {
    position: absolute; left: 38px; bottom: 30px;
    list-style: none; display: flex; flex-direction: column; gap: 7px;
  }
  .contacts li {
    display: flex; align-items: center; gap: 9px;
    font-size: 14px; font-weight: 500; color: var(--grey-text);
  }
  .contacts svg { width: 14px; height: 14px; flex: none; }

  .card--back .brand {
    position: absolute; left: 0; right: 0; top: 0; bottom: 0;
    justify-content: center;
    font-size: 32px; color: var(--paper);
  }
  .card--back .brand__dot { width: 24px; height: 24px; background: var(--paper); }
</style>
</head>
<body>
<main class="sheet">
  <section class="card card--front" aria-label="Card front">
    <div class="corner-tab"></div>
    <div class="holder">
      <p class="holder__name">Derek L. <span class="surname">Whitmore</span></p>
      <p class="holder__title">CPA CGMA</p>
    </div>

    <div class="brand">
      <span class="brand__dot"></span>
      <span class="brand__name">Brovant Advisory</span>
    </div>

    <ul class="contacts">
      <li>
        <svg viewBox="0 0 16 16" aria-hidden="true"><circle cx="8" cy="8" r="8" fill="var(--teal)"/><path d="M5.2 4.2l1.5 0 .6 2-1 .8c.5 1.1 1.3 1.9 2.4 2.4l.8-1 2 .6v1.5c0 .5-.4.8-.9.8C7.2 11.2 4.8 8.8 4.4 5.1c0-.5.3-.9.8-.9z" fill="#fff"/></svg>
        <span>555-014-2283</span>
      </li>
      <li>
        <svg viewBox="0 0 16 16" aria-hidden="true"><rect x="1" y="3" width="14" height="10" rx="1.5" fill="var(--teal)"/><path d="M1.8 4l6.2 4.8L14.2 4" fill="none" stroke="#fff" stroke-width="1.3"/></svg>
        <span>dwhitmore@brovantadvisory.example</span>
      </li>
      <li>
        <svg viewBox="0 0 16 16" aria-hidden="true"><circle cx="8" cy="8" r="7" fill="var(--teal)"/><g fill="none" stroke="#fff" stroke-width="1"><ellipse cx="8" cy="8" rx="3" ry="7"/><path d="M1 8h14"/></g></svg>
        <span>www.brovantadvisory.example</span>
      </li>
    </ul>
  </section>

  <section class="card card--back" aria-label="Card back">
    <div class="brand">
      <span class="brand__dot"></span>
      <span class="brand__name">Brovant Advisory</span>
    </div>
  </section>
</main>
</body>
</html>
```